Velmoria - 3D medical animations and high end visual content

Our company creates high end visual content and animations for medical global companies.
Our website - www.velmoria-studio.example
We would like to have an amazing business card for our CEO that he can use in the following exhebitions he is going to attend.
It is very important that the design will be memorable and diffrent. It has to reflect our brand design (you can have it from our website)
We would like to transmit innovation, prestige, luxury, aesthetics.
The card has to be Double Sided

Target Market(s)

Marketing managers in medical global companys

Industry/Entity Type

It Company

Contact Information for Business Card

Requirements
Nice to have
• It is very important that the design will be memorable and diffrent. It has to reflect our brand design (you can have it from our website)

```html
<!DOCTYPE html>
<html lang="en">
<head>
<meta charset="utf-8">
<title>Velmoria – Business Card</title>
<link rel="stylesheet" href="https://fonts.googleapis.com/css2?family=Open+Sans:wght@400;600;700&display=swap">
<style>
  :root {
    --teal: #1596b0;
    --teal-light: #2aa9c2;
    --teal-dark: #0f7f98;
    --white: #ffffff;
    --ink: #2b2b2b;
    --ink-soft: #555b60;
    --page: #eceeef;
  }
  * { box-sizing: border-box; margin: 0; padding: 0; }
  html, body { width: 1200px; height: 1000px; overflow: hidden; }
  body {
    background: var(--page);
    font-family: "Open Sans", Arial, sans-serif;
    position: relative;
  }
  .card {
    position: absolute;
    left: 250px;
    width: 700px;
    height: 400px;
    border-radius: 6px;
    overflow: hidden;
    box-shadow: 0 8px 24px rgba(0,0,0,0.14);
  }
  .card--back {
    top: 60px;
    background: linear-gradient(135deg, var(--teal-light), var(--teal) 55%, var(--teal-dark));
    display: flex;
    align-items: center;
    justify-content: center;
  }
  .brand-name {
    font-family: "Open Sans", Arial, sans-serif;
    font-weight: 600;
    letter-spacing: 0.08em;
    text-transform: uppercase;
  }
  .card--back .brand-name { color: var(--white); font-size: 56px; }

  .card--front { top: 540px; background: var(--teal); }
  .card-shape { position: absolute; inset: 0; }
  .front-logo {
    position: absolute;
    left: 48px;
    top: 150px;
    color: var(--ink);
    font-size: 34px;
  }
  .divider {
    position: absolute;
    left: 330px;
    top: 110px;
    width: 2px;
    height: 190px;
    background: var(--teal);
  }
  .contact {
    position: absolute;
    left: 360px;
    top: 110px;
  }
  .contact-name {
    color: var(--teal);
    font-size: 27px;
    font-weight: 600;
    line-height: 1.1;
  }
  .contact-title {
    color: var(--ink);
    font-size: 15px;
    font-weight: 600;
    margin-bottom: 22px;
  }
  .contact-row {
    display: flex;
    align-items: center;
    gap: 14px;
    color: var(--ink-soft);
    font-size: 15px;
    height: 32px;
  }
  .contact-row svg { width: 18px; height: 18px; flex: none; }
  .website {
    position: absolute;
    right: 40px;
    bottom: 16px;
    color: var(--white);
    font-size: 16px;
    letter-spacing: 0.02em;
  }
</style>
</head>
<body>

  <section class="card card--back" aria-label="Card back">
    <span class="brand-name">Velmoria</span>
  </section>

  <section class="card card--front" aria-label="Card front">
    <svg class="card-shape" viewBox="0 0 700 400" preserveAspectRatio="none" aria-hidden="true">
      <polygon fill="#ffffff" points="0,40 300,40 340,14 700,14 700,330 420,330 380,356 0,356"/>
    </svg>

    <span class="brand-name front-logo">Velmoria</span>
    <div class="divider"></div>

    <div class="contact">
      <p class="contact-name">Aron Leval</p>
      <p class="contact-title">Founder &amp; CEO</p>

      <p class="contact-row">
        <svg viewBox="0 0 24 24" aria-hidden="true"><rect x="6" y="2" width="12" height="20" rx="2" fill="none" stroke="#1596b0" stroke-width="2"/><circle cx="12" cy="18" r="1.2" fill="#1596b0"/></svg>
        +972-52-5550147
      </p>
      <p class="contact-row">
        <svg viewBox="0 0 24 24" aria-hidden="true"><path d="M6.6 10.8a15 15 0 0 0 6.6 6.6l2.2-2.2a1 1 0 0 1 1-.25 11.4 11.4 0 0 0 3.6.57 1 1 0 0 1 1 1V20a1 1 0 0 1-1 1A17 17 0 0 1 3 4a1 1 0 0 1 1-1h3.5a1 1 0 0 1 1 1c0 1.25.2 2.45.57 3.57a1 1 0 0 1-.25 1z" fill="#1596b0"/></svg>
        +972-77-5550283
      </p>
      <p class="contact-row">
        <svg viewBox="0 0 24 24" aria-hidden="true"><rect x="2" y="5" width="20" height="14" rx="1" fill="#1596b0"/><path d="M3 6l9 7 9-7" fill="none" stroke="#ffffff" stroke-width="1.6"/></svg>
        aron@velmoria-studio.example
      </p>
    </div>

    <span class="website">www.velmoria-studio.example</span>
  </section>

</body>
</html>
```